Visitenkarten-Design für K17.eu - TradeWing Finanz
Zielgruppe
Smartphone-Banking mit Mehrwert
Aufgabenstellung
Bitte entwerfen Sie kreative Visitenkarten für uns.
- Halten Sie einen Platz/Rahmen frei für Fotos, die wir nachträglich einsetzen, und kennzeichnen diesen.
- Halten Sie einen Patz/Rahmen für Vor- und Nachname sowie für die Berufsbezeichnung frei und kennzeichnen diesen.
- Halten Sie einen Platz/Rahmen für die Telefonnummern und die Email-Adressen frei und kennzeichnen diesen.
Alle Visitenkarten sollen folgende Daten beinhalten:
Vorname Nachname*
Berufsbezeichnung*
Mobile:
Office:
Email:
Domain:
* = individuell, jeder Mitarbeiter hat eigene Daten
Die Farben müssen sich an unserem CI-Design orientieren, orange/weiß/schwarz/grau -
Außerdem finden Sie unser Logo in der Anlage, welches Sie bitte auf der Karte platzieren.
Bitte liefern Sie uns die Designs in verschiedenen Formaten - psd, ai, eps, jpg, png
Bei Fragen zögern Sie nicht, uns zu kontaktieren. Danke.

```html
<!DOCTYPE html>
<html lang="de">
<head>
<meta charset="utf-8">
<title>K17.eu – Visitenkarte</title>
<link href="https://fonts.googleapis.com/css2?family=Arimo:wght@400;700&display=swap" rel="stylesheet">
<style>
  :root {
    --bg: #e5e4e2;
    --card-black: #1a1918;
    --orange: #d57a36;
    --white: #ffffff;
    --grey-text: #5e5e5e;
    --frame-grey: #3a3a3a;
  }
  html, body {
    margin: 0;
    padding: 0;
    width: 1200px;
    height: 938px;
    overflow: hidden;
    background: var(--bg);
    font-family: "Arimo", Arial, sans-serif;
  }
  .canvas { position: relative; width: 1200px; height: 938px; }

  .card {
    position: absolute;
    background: var(--card-black);
    border-radius: 42px;
  }
  .card-front { left: 118px; top: 145px; width: 420px; height: 648px; }
  .card-back  { left: 665px; top: 145px; width: 417px; height: 645px; }

  .earpiece-camera {
    position: absolute; left: 157px; top: 33px;
    width: 11px; height: 11px; border-radius: 50%; background: var(--frame-grey);
  }
  .earpiece-dot {
    position: absolute; left: 208px; top: 15px;
    width: 8px; height: 8px; border-radius: 50%; background: var(--frame-grey);
  }
  .earpiece-slot {
    position: absolute; left: 187px; top: 35px;
    width: 50px; height: 6px; border-radius: 3px; background: var(--frame-grey);
  }
  .home-button {
    position: absolute; left: 186px; top: 582px;
    width: 48px; height: 48px; border-radius: 50%;
    border: 2px solid var(--frame-grey); box-sizing: border-box;
  }

  .screen {
    position: absolute; left: 11px; top: 79px;
    width: 400px; height: 490px;
    background: var(--white); overflow: hidden;
  }
  .header-wave { position: absolute; left: 0; top: 0; }

  .brand-front {
    position: absolute; left: 22px; top: 16px;
    color: var(--white); font-weight: 700; font-size: 34px; letter-spacing: 0.5px;
  }
  .brand-front-url {
    position: absolute; left: 22px; top: 58px;
    color: var(--white); font-weight: 700; font-size: 16px;
  }
  .menu-icon { position: absolute; left: 346px; top: 30px; }

  .company {
    position: absolute; left: 22px; top: 162px;
    color: var(--grey-text); font-size: 20px; line-height: 27px;
  }
  .company strong { font-weight: 700; }

  .person { position: absolute; left: 22px; top: 294px; }
  .person-name {
    margin: 0; color: var(--orange); font-weight: 700; font-size: 24px; line-height: 32px;
  }
  .person-role {
    margin: 0; color: var(--grey-text); font-size: 20px; line-height: 30px;
  }

  .contact-icons { position: absolute; left: 22px; top: 376px; }
  .contact-list {
    position: absolute; left: 73px; top: 379px;
    margin: 0; padding: 0; list-style: none;
    color: var(--grey-text); font-size: 20px; line-height: 28.5px;
  }

  .photo-slot {
    position: absolute; left: 283px; top: 302px; width: 110px; height: 155px;
    background: linear-gradient(160deg, #e9e7e6 0%, #c9b9ad 45%, #6e5440 75%, #2a2624 100%);
  }

  .brand-back {
    position: absolute; left: 0; right: 0; top: 205px; text-align: center;
    color: var(--orange); font-weight: 700; font-size: 64px; letter-spacing: 1px;
  }
  .brand-back-url {
    position: absolute; left: 0; right: 0; top: 290px; text-align: center;
    color: var(--white); font-weight: 700; font-size: 28px;
  }
</style>
</head>
<body>
<main class="canvas">

  <section class="card card-front" aria-label="Vorderseite">
    <span class="earpiece-dot"></span>
    <span class="earpiece-camera"></span>
    <span class="earpiece-slot"></span>

    <div class="screen">
      <svg class="header-wave" width="400" height="150" viewBox="0 0 400 150" aria-hidden="true">
        <path d="M0 0 H400 V140 C360 146 320 140 270 122 C210 100 160 96 120 100 C70 105 30 114 0 120 Z" fill="var(--orange)"/>
      </svg>
      <div class="brand-front">K17</div>
      <div class="brand-front-url">www.k17.eu</div>
      <svg class="menu-icon" width="30" height="26" viewBox="0 0 30 26" aria-hidden="true">
        <rect x="0" y="0" width="30" height="4" fill="var(--white)"/>
        <rect x="0" y="11" width="30" height="4" fill="var(--white)"/>
        <rect x="0" y="22" width="30" height="4" fill="var(--white)"/>
      </svg>

      <address class="company" style="font-style:normal">
        <strong>K17 GmbH</strong><br>
        Lindenweg 12<br>
        93047 Regensburg<br>
        Germany
      </address>

      <div class="person">
        <p class="person-name">Vorname Nachname</p>
        <p class="person-role">Berufsbezeichnung</p>
      </div>

      <svg class="contact-icons" width="32" height="104" viewBox="0 0 32 104" aria-hidden="true">
        <rect x="1.5" y="1.5" width="29" height="48" rx="3" fill="none" stroke="var(--orange)" stroke-width="2"/>
        <line x1="1.5" y1="8" x2="30.5" y2="8" stroke="var(--orange)" stroke-width="1.5"/>
        <line x1="1.5" y1="41" x2="30.5" y2="41" stroke="var(--orange)" stroke-width="1.5"/>
        <line x1="12" y1="5" x2="20" y2="5" stroke="var(--orange)" stroke-width="1.5"/>
        <circle cx="16" cy="45" r="1.6" fill="var(--orange)"/>
        <rect x="1" y="80" width="30" height="21" fill="none" stroke="var(--orange)" stroke-width="2"/>
        <polyline points="1,80 16,93 31,80" fill="none" stroke="var(--orange)" stroke-width="2"/>
        <line x1="1" y1="101" x2="12" y2="89" stroke="var(--orange)" stroke-width="1.5"/>
        <line x1="31" y1="101" x2="20" y2="89" stroke="var(--orange)" stroke-width="1.5"/>
      </svg>
      <ul class="contact-list">
        <li>+49 171 xxxxxxx</li>
        <li>+49 941 xxxxxx-xx</li>
        <li>vorname@k17.eu</li>
      </ul>

      <div class="photo-slot" role="img" aria-label="Platzhalter für Mitarbeiterfoto"></div>
    </div>

    <span class="home-button"></span>
  </section>

  <section class="card card-back" aria-label="Rückseite">
    <div class="brand-back">K17</div>
    <div class="brand-back-url">www.k17.eu</div>
  </section>

</main>
</body>
</html>
```